Brand Identity & Marketing Website Design for Professional Football Fieldnote Software

KestrelPane is a professional football scouting report generation software.
It is a standalone desktop application that allows football clubs, agencies and players to generate structured, executive-level A4 PDF scouting reports.
This is NOT:
a betting platform
a fan website
a football news blog
a SaaS subscription platform
This is a premium document-generation software tool designed for professional use inside football organizations.
The brand must reflect:
• Structure
• Authority
• Precision
• Professionalism
• Trust
• Executive-level quality
Think consulting firm, performance analysis tool, structured business software.
Not flashy sports media.
What We Need
We are looking for:
1️⃣ Logo Design
2️⃣ Full Brand Identity System
3️⃣ Marketing Website UI/UX Design
(Development is NOT included in this job.)
Important Product Context
KestrelPane is sold as a one-time purchase software package.
After purchase: • Customers download the software
• Install it locally
• Generate reports offline
There is no recurring subscription.
There is no SaaS login platform.
The website is a marketing and purchase website only.
1️⃣ Logo Design
The logo must:
• Be professional and timeless
• Work in both light and dark backgrounds
• Be scalable (website header, app icon, favicon)
• Avoid cliché football logo styles (no shields, mascots, flashy emblems)
• Feel modern, clean, and strong
We prefer:
• Clean typography-based logo
• Minimal symbol integration
• Strong visual balance
• Suitable for software branding
Name:
KestrelPane
Optional tagline:
The leading platform for professional football scouting reports
Deliver:
• Full logo
• Icon-only version (for desktop app icon)
• Light & dark variations
2️⃣ Brand Identity System
We need a structured design system that supports:
• Marketing website
• Desktop application UI
• PDF report previews
Please define:
• Primary color palette
• Secondary color palette
• Accent colors
• Typography system (professional, highly readable)
• Heading hierarchy
• UI styling guidelines
• Light mode & dark mode principles
The design must feel:
• Minimal
• Grid-based
• Clean
• Premium
• Corporate
Avoid:
• Neon colors
• Heavy gradients
• Overly sporty visuals
• Gaming aesthetics
3️⃣ Marketing Website Design (UI/UX Only)
We need full website design in Figma for:
• Homepage
• Product Overview
• Packages Page (Club / Agency / Player)
• How It Works
• Demo Section
• FAQ
• Contact
• Purchase / Download Page
Design must include:
• Hero section
• Feature explanation sections
• Structured benefits
• Product screenshots placement
• Pricing comparison layout
• Clear call-to-action areas
• Professional footer
Responsive design required (Desktop-first, mobile adaptation).
Important:
Content copy will be provided by us.
Designer focuses on layout, structure, hierarchy and visual design.
Target Audience
• Professional football clubs
• Scouting departments
• Player agencies
• Semi-professional and professional players
This is primarily B2B, with some B2C.
Style Direction
We are looking for:
• Strong typography
• Balanced whitespace
• Structured layouts
• Subtle but confident use of color
• Professional photography (if used)
• Premium software feel
The website and brand must feel trustworthy and high-level.
Deliverables
• Logo files (AI, SVG, PNG)
• Brand guideline document (PDF)
• Figma file with full website UI
• Icon assets (app icon, favicon)
• Color and typography system

Need extra days to review

```html
<!DOCTYPE html>
<html lang="en">
<head>
<meta charset="utf-8">
<title>KestrelPane — Professional Football Scouting Reports</title>
<link rel="stylesheet" href="https://fonts.googleapis.com/css2?family=Open+Sans:wght@400;500;600;700;800&display=swap">
<style>
:root{
  --primary:#1f4796;
  --primary-dark:#1a3c86;
  --ink:#141414;
  --muted:#4b4b4b;
  --line:#dfe2e8;
  --soft-bg:#f1f1f3;
  --table-head:#e6ecf5;
  --green:#22b14c;
  --footer:#2b2b2b;
  --white:#ffffff;
}
*{box-sizing:border-box;margin:0;padding:0}
html,body{width:1200px;height:3665px;overflow:hidden}
body{font-family:"Open Sans",Arial,sans-serif;color:var(--ink);background:var(--white);position:relative}
.abs{position:absolute}
.section-title{position:absolute;left:0;width:1200px;text-align:center;font-size:36px;font-weight:400;color:var(--ink)}
.section-title b{font-weight:700}
.title-rule{position:absolute;left:582px;width:36px;height:3px;background:var(--ink)}

/* header */
.site-header{position:absolute;top:0;left:0;width:1200px;height:77px;background:var(--white);box-shadow:0 2px 6px rgba(0,0,0,.12);z-index:2}
.brand{position:absolute;left:101px;top:20px;font-size:24px;font-weight:400}
.brand b{font-weight:700}
.main-nav{position:absolute;left:374px;top:26px;display:flex;gap:0;font-size:15px;color:#333}
.main-nav span{margin-right:29px}
.main-nav .active{color:var(--primary);font-weight:700}
.btn-quote{position:absolute;left:979px;top:14px;width:121px;height:43px;border-radius:22px;background:var(--primary);color:#fff;font-size:15px;font-weight:600;display:flex;align-items:center;justify-content:center}

/* hero */
.hero{position:absolute;top:77px;left:0;width:1200px;height:592px;background:linear-gradient(100deg,#f4f5f7 0%,#eef1f4 30%,#d3dce4 55%,#b9c7d4 80%,#a9b9c8 100%)}
.hero-photo{position:absolute;left:560px;top:0;width:640px;height:592px;background:linear-gradient(160deg,#c7d3de 0%,#dbe3ea 40%,#aebfcf 100%);opacity:.85}
.hero h1{position:absolute;left:110px;top:118px;font-size:46px;line-height:51px;font-weight:400;color:var(--ink)}
.hero h1 b{font-weight:800;letter-spacing:.5px}
.hero p{position:absolute;left:112px;top:282px;width:420px;font-size:16px;line-height:26px;color:var(--ink)}
.btn{position:absolute;height:50px;border-radius:25px;display:flex;align-items:center;justify-content:center;font-size:16px;font-weight:600}
.btn-solid{background:var(--primary);color:#fff}
.btn-outline{border:2px solid var(--primary);color:var(--primary);background:rgba(255,255,255,.6)}

/* features */
.features{position:absolute;top:669px;left:0;width:1200px;height:448px;background:var(--soft-bg)}
.feature-card{position:absolute;top:172px;width:296px;height:201px;background:#fff;border-radius:4px;box-shadow:0 2px 8px rgba(0,0,0,.08);padding:14px 22px}
.feature-head{display:flex;gap:12px;align-items:flex-start;height:60px;border-bottom:1px solid var(--line)}
.feature-head h3{font-size:16px;line-height:25px;font-weight:500}
.feature-card p{margin-top:16px;font-size:13px;line-height:24px;color:var(--muted)}

/* product overview */
.laptop-shot{position:absolute;left:65px;top:1318px;width:502px;height:300px}
.overview-copy{position:absolute;left:598px;top:1306px;width:480px}
.overview-copy h3{font-size:20px;font-weight:700}
.overview-copy p{margin-top:12px;font-size:15.5px;line-height:26px;color:var(--muted)}
.check-list{list-style:none;margin-top:16px}
.check-list li{display:flex;align-items:center;gap:10px;font-size:16px;font-weight:500;height:32px}

/* packages */
.package-table{position:absolute;left:111px;top:1890px;width:978px;height:334px;border:1px solid var(--line);border-radius:12px;overflow:hidden;border-collapse:separate}
.pkg-row{display:flex;height:84px;border-top:1px solid var(--line)}
.pkg-row:first-child{border-top:none;height:82px;background:var(--table-head)}
.pkg-cell{display:flex;align-items:center;justify-content:center;text-align:center;border-left:1px solid var(--line);font-size:13px;line-height:21px;color:#333}
.pkg-cell:first-child{border-left:none}
.c1{width:241px}.c2{width:247px}.c3{width:244px}.c4{width:246px}
.pkg-row:first-child .pkg-cell{font-size:20px;font-weight:700;color:var(--primary)}
.pkg-name{font-size:19px !important;font-weight:500;color:var(--ink) !important}

/* demo band */
.demo-band{position:absolute;top:2322px;left:0;width:1200px;height:291px;background:linear-gradient(90deg,#1d3f8f 0%,#21469a 60%,#1d418f 100%)}
.demo-band h2{position:absolute;left:0;width:1200px;top:43px;text-align:center;font-size:36px;font-weight:400;color:#fff}
.demo-band h2 b{font-weight:700}
.demo-band .rule{position:absolute;left:582px;top:98px;width:36px;height:3px;background:#fff}
.demo-band p{position:absolute;left:0;width:1200px;top:131px;text-align:center;font-size:17px;font-weight:600;color:#fff}
.btn-light{background:#f3f3f3;color:var(--ink);font-weight:500}
.btn-ghost{border:2px solid #fff;color:#fff;font-weight:500}

/* faq */
.faq-item{position:absolute;left:111px;width:978px;height:55px;border:1px solid var(--line);border-radius:6px;display:flex;align-items:center;padding:0 20px;font-size:16px;color:#222}
.faq-item svg{position:absolute;right:19px;top:17px}
.faq-open{background:var(--primary);color:#fff;height:86px;align-items:flex-start;flex-direction:column;justify-content:center;gap:8px;border-color:var(--primary)}
.faq-open .answer{font-size:15px}

/* footer */
.site-footer{position:absolute;top:3281px;left:0;width:1200px;height:384px;background:var(--footer);color:#fff}
.footer-brand{position:absolute;left:0;width:1200px;top:68px;text-align:center;font-size:40px;font-weight:400}
.footer-brand b{font-weight:700}
.footer-nav{position:absolute;left:0;width:1200px;top:151px;text-align:center;font-size:17px}
.footer-nav span{margin:0 17px}
.contact{position:absolute;top:225px;display:flex;align-items:center;gap:16px}
.contact .icon{width:62px;height:62px;border:2px solid #fff;border-radius:50%;display:flex;align-items:center;justify-content:center}
.contact small{display:block;font-size:15px;color:#ddd}
.contact strong{display:block;font-size:17px;font-weight:600;margin-top:6px}
.copyright{position:absolute;left:0;width:1200px;top:318px;text-align:center;font-size:16px}
</style>
</head>
<body>

<header class="site-header">
  <div class="brand">Fieldnote <b>Software</b></div>
  <nav class="main-nav">
    <span class="active">Home</span><span>Product</span><span>Packages</span><span>How It Works</span><span>FAQ</span><span>Contact</span><span>Purchase</span>
  </nav>
  <div class="btn-quote">Get a Quote</div>
</header>

<section class="hero">
  <div class="hero-photo" role="img" aria-label="Photo of a laptop screen showing analytics dashboards with charts"></div>
  <h1>Professional Football<br><b>Scouting Reports.<br>Elevated.</b></h1>
  <p>The leading platform for structured, executive-level football scouting reports — trusted by clubs, agencies, and professionals.</p>
  <div class="btn btn-solid" style="left:111px;top:383px;width:167px">Download Demo</div>
  <div class="btn btn-outline" style="left:296px;top:383px;width:192px">View Sample Report</div>
</section>

<section class="features">
  <h2 class="section-title" style="top:67px">Our Core <b>Features</b></h2>
  <div class="title-rule" style="top:124px"></div>

  <article class="feature-card" style="left:111px">
    <div class="feature-head">
      <svg width="30" height="32" viewBox="0 0 30 32"><rect x="2" y="2" width="22" height="28" rx="2" fill="none" stroke="#1f4796" stroke-width="2.5"/><rect x="14" y="16" width="14" height="14" fill="#1f4796"/><rect x="17" y="23" width="2" height="5" fill="#fff"/><rect x="21" y="20" width="2" height="8" fill="#fff"/><line x1="6" y1="9" x2="16" y2="9" stroke="#1f4796" stroke-width="2"/></svg>
      <h3>Structured Scouting Report Builder</h3>
    </div>
    <p>Create professional, standardized football scouting reports using guided templates designed for consistent and detailed player analysis.</p>
  </article>

  <article class="feature-card" style="left:453px">
    <div class="feature-head">
      <svg width="30" height="30" viewBox="0 0 30 30"><rect x="1" y="3" width="28" height="26" rx="3" fill="#1f4796"/><path d="M15 23V10M9.5 15.5 15 10l5.5 5.5" stroke="#fff" stroke-width="2.5" fill="none"/></svg>
      <h3>Executive-Level A4 PDF Export</h3>
    </div>
    <p>Generate clean, presentation-ready A4 PDF reports instantly for recruitment decisions and professional player presentations.</p>
  </article>

  <article class="feature-card" style="left:793px">
    <div class="feature-head">
      <svg width="34" height="32" viewBox="0 0 34 32"><rect x="2" y="2" width="30" height="21" rx="2" fill="none" stroke="#1f4796" stroke-width="2.5"/><rect x="6" y="6" width="22" height="13" fill="#1f4796"/><rect x="12" y="26" width="10" height="3" fill="#1f4796"/></svg>
      <h3>Fully Offline Desktop Software</h3>
    </div>
    <p>Runs fully offline on your computer, keeping all scouting data secure while allowing scouts and analysts to work anywhere without internet access.</p>
  </article>
</section>

<section class="overview">
  <h2 class="section-title" style="top:1196px">Product <b>Overview</b></h2>
  <div class="title-rule" style="top:1253px"></div>

  <div class="laptop-shot">
    <svg width="502" height="300" viewBox="0 0 502 300">
      <rect x="36" y="0" width="432" height="288" rx="12" fill="#2a2c30"/>
      <rect x="46" y="14" width="412" height="266" fill="#f4f6fa" role="img" aria-label="Dashboard screen of the scouting application"/>
      <rect x="46" y="14" width="412" height="20" fill="#e8edf5"/>
      <text x="56" y="29" font-family="Open Sans, sans-serif" font-size="9" font-weight="700" fill="#1f4796">DASHBOARD</text>
      <polyline points="90,115 120,100 150,112 180,95 210,108 240,98 270,110 300,92 330,104 360,96 400,106 430,98" fill="none" stroke="#3d7bd9" stroke-width="1.5"/>
      <polyline points="90,125 120,120 150,128 180,115 210,124 240,118 270,126 300,114 330,122 360,116 400,124 430,118" fill="none" stroke="#d94c5a" stroke-width="1.5"/>
      <circle cx="390" cy="185" r="22" fill="#8fb8e8"/>
      <path d="M390 185 L390 163 A22 22 0 0 1 410 194 Z" fill="#d4a0e0"/>
      <rect x="90" y="230" width="120" height="8" fill="#9cc8e8"/>
      <rect x="230" y="230" width="90" height="8" fill="#9cc8e8"/>
      <rect x="90" y="250" width="100" height="8" fill="#9cc8e8"/>
      <rect x="0" y="288" width="502" height="12" rx="4" fill="#54575c"/>
    </svg>
  </div>

  <div class="overview-copy">
    <h3>A Professional Workflow, Refined.</h3>
    <p>KestrelPane is engineered for speed, clarity, and reporting accuracy. Every layout, field, and action is optimized for analysts and scouts.</p>
    <ul class="check-list">
      <li><svg width="16" height="16"><circle cx="8" cy="8" r="8" fill="var(--green)"/><path d="M4.5 8.2l2.3 2.3 4.5-4.6" stroke="#fff" stroke-width="1.8" fill="none"/></svg>Dashboard</li>
      <li><svg width="16" height="16"><circle cx="8" cy="8" r="8" fill="var(--green)"/><path d="M4.5 8.2l2.3 2.3 4.5-4.6" stroke="#fff" stroke-width="1.8" fill="none"/></svg>Player Report Screen</li>
      <li><svg width="16" height="16"><circle cx="8" cy="8" r="8" fill="var(--green)"/><path d="M4.5 8.2l2.3 2.3 4.5-4.6" stroke="#fff" stroke-width="1.8" fill="none"/></svg>Match Analysis Screen</li>
      <li><svg width="16" height="16"><circle cx="8" cy="8" r="8" fill="var(--green)"/><path d="M4.5 8.2l2.3 2.3 4.5-4.6" stroke="#fff" stroke-width="1.8" fill="none"/></svg>PDF Export Preview</li>
    </ul>
  </div>
  <div class="btn btn-solid" style="left:599px;top:1580px;width:148px;height:51px;font-size:15px">Read More</div>
</section>

<section class="packages">
  <h2 class="section-title" style="top:1783px">Choose Your <b>KestrelPane Package</b></h2>
  <div class="title-rule" style="top:1840px"></div>
  <div class="package-table">
    <div class="pkg-row"><div class="pkg-cell c1">LICENSE</div><div class="pkg-cell c2">BEST FOR</div><div class="pkg-cell c3">INCLUDES</div><div class="pkg-cell c4">PURCHASE</div></div>
    <div class="pkg-row"><div class="pkg-cell c1 pkg-name">Club License</div><div class="pkg-cell c2">Professional clubs<br>&amp; academies</div><div class="pkg-cell c3">Full Scouting Tools, Multi-<br>department usage</div><div class="pkg-cell c4">One-time purchase —<br><b>No subscriptions</b></div></div>
    <div class="pkg-row"><div class="pkg-cell c1 pkg-name">Agency License</div><div class="pkg-cell c2">Player management &amp;<br>representation</div><div class="pkg-cell c3">Player comparison tools, Transfer<br>-focused reporting</div><div class="pkg-cell c4">One-time purchase</div></div>
    <div class="pkg-row"><div class="pkg-cell c1 pkg-name">Player License</div><div class="pkg-cell c2">Individual players building<br>professional profiles</div><div class="pkg-cell c3">Player profile builder, Self-<br>assessment tools</div><div class="pkg-cell c4">One-time purchase</div></div>
  </div>
</section>

<section class="demo-band">
  <h2>See KestrelPane <b>in Action</b></h2>
  <div class="rule"></div>
  <p>Watch a short walkthrough demonstrating the full reporting workflow and export process.</p>
  <div class="btn btn-light" style="left:434px;top:183px;width:138px">Watch Demo</div>
  <div class="btn btn-ghost" style="left:593px;top:183px;width:173px">View Sample PDF</div>
</section>

<section class="faq">
  <h2 class="section-title" style="top:2686px">Frequently <b>Asked Questions</b></h2>
  <div class="title-rule" style="top:2743px"></div>
  <div class="faq-item" style="top:2790px">1) Is KestrelPane a subscription?<svg width="20" height="20"><circle cx="10" cy="10" r="9" fill="none" stroke="#777"/><path d="M10 5v10M5 10h10" stroke="#777"/></svg></div>
  <div class="faq-item" style="top:2855px">2) Does it require internet?<svg width="20" height="20"><circle cx="10" cy="10" r="9" fill="none" stroke="#777"/><path d="M10 5v10M5 10h10" stroke="#777"/></svg></div>
  <div class="faq-item" style="top:2920px">3) Can I customize the reports? Is this for professional clubs only?<svg width="20" height="20"><circle cx="10" cy="10" r="9" fill="none" stroke="#777"/><path d="M10 5v10M5 10h10" stroke="#777"/></svg></div>
  <div class="faq-item faq-open" style="top:2985px"><span>4) Does the software require an internet connection?</span><span class="answer">No. KestrelPane works completely offline, allowing scouts and analysts to work securely without cloud dependency.</span><svg width="20" height="20"><circle cx="10" cy="10" r="10" fill="#fff"/><path d="M5 10h10" stroke="#1f4796" stroke-width="2"/></svg></div>
  <div class="faq-item" style="top:3079px">5) Who is KestrelPane designed for?<svg width="20" height="20"><circle cx="10" cy="10" r="9" fill="none" stroke="#777"/><path d="M10 5v10M5 10h10" stroke="#777"/></svg></div>
  <div class="faq-item" style="top:3144px">6) What type of reports can be generated?s only?<svg width="20" height="20"><circle cx="10" cy="10" r="9" fill="none" stroke="#777"/><path d="M10 5v10M5 10h10" stroke="#777"/></svg></div>
</section>

<footer class="site-footer">
  <div class="footer-brand">Fieldnote <b>Software</b></div>
  <nav class="footer-nav"><span>Home</span><span>Product</span><span>Packages</span><span>How It Works</span><span>FAQ</span><span>Contact</span><span>Purchase</span></nav>
  <div class="contact" style="left:111px">
    <div class="icon"><svg width="24" height="30" viewBox="0 0 24 30"><path d="M12 1C6 1 1.5 5.5 1.5 11.3 1.5 19 12 29 12 29s10.5-10 10.5-17.7C22.5 5.5 18 1 12 1z" fill="#fff"/><circle cx="12" cy="11" r="4" fill="#2b2b2b"/></svg></div>
    <div><small>Location</small><strong>Fieldnote Software, US</strong></div>
  </div>
  <div class="contact" style="left:455px">
    <div class="icon"><svg width="28" height="20" viewBox="0 0 28 20"><rect width="28" height="20" rx="2" fill="#fff"/><path d="M1 2l13 9 13-9" stroke="#2b2b2b" stroke-width="2" fill="none"/></svg></div>
    <div><small>Email Address</small><strong>info@fieldnotesoftware.example</strong></div>
  </div>
  <div class="contact" style="left:873px">
    <div class="icon"><svg width="28" height="28" viewBox="0 0 28 28"><path d="M6 2l5 5-3 3c1.5 4 5 7.5 9 9l3-3 5 5-3 4C12 24 4 16 2 6z" fill="#fff"/></svg></div>
    <div><small>Call Us</small><strong>+1 555 014 2290</strong></div>
  </div>
  <div class="copyright">Copyrights2026.Fieldnote Software.All Rights Reserved</div>
</footer>

</body>
</html>
```